Launching new podcast and need artwork

we are two guys in our early 40's from east Texas who are starting a podcast around personal finance.

The title of the podcast will be "Coin Porchlight" and the subtitle will be "Money tricks with a little front-porch drawl"

We own the company brightharborplans.com and will be using the podcast as a lead generation for our primary business of financial coaching.

Target Market(s)

Male 35-45 years old

Industry/Entity Type

Personal finance

Requirements
Nice to have
• Rugged or rustic feel would fit our personas

```html
<!DOCTYPE html>
<html lang="en">
<head>
<meta charset="utf-8">
<title>Coin Porchlight – Podcast Artwork</title>
<link rel="stylesheet" href="https://fonts.googleapis.com/css2?family=Anton&family=Poppins:wght@300;400;700&display=swap">
<style>
  :root {
    --page: #dcdcdc;
    --denim: #36608f;
    --denim-deep: #24436b;
    --denim-light: #4b77a8;
    --leaf: #7dba45;
    --chalk: #ffffff;
    --photo-light: #b4b4b4;
    --photo-mid: #5a5a5a;
    --photo-dark: #1c1c1c;
  }
  * { margin: 0; padding: 0; box-sizing: border-box; }
  html, body {
    width: 1200px; height: 1058px; overflow: hidden;
    background: var(--page);
  }
  .cover {
    position: absolute; left: 168px; top: 98px;
    width: 864px; height: 864px; overflow: hidden;
    background:
      radial-gradient(ellipse at 25% 15%, var(--denim-light) 0%, transparent 55%),
      radial-gradient(ellipse at 85% 95%, var(--denim-deep) 0%, transparent 60%),
      var(--denim);
    box-shadow: 0 10px 30px rgba(0,0,0,.18);
  }
  .grunge, .hosts-photo, .frame-lines { position: absolute; inset: 0; }
  .grunge { mix-blend-mode: overlay; opacity: .55; }
  .title {
    position: absolute; left: 36px; display: block;
    font-family: "Anton", sans-serif; line-height: 1; text-transform: uppercase;
  }
  .title-top { top: 14px; font-size: 196px; color: var(--chalk); letter-spacing: 2px; }
  .title-bottom { top: 265px; font-size: 112px; color: var(--leaf); letter-spacing: 1px; }
  .tagline {
    position: absolute; left: 40px; width: 374px; text-align: center;
    font-family: "Poppins", sans-serif; text-transform: uppercase; line-height: 1;
  }
  .tagline-main { top: 454px; font-size: 34px; font-weight: 300; color: var(--chalk); }
  .tagline-join { top: 510px; font-size: 26px; font-weight: 400; color: var(--leaf); }
  .tagline-end { top: 552px; font-size: 22px; font-weight: 700; color: var(--chalk); }
  .brand {
    position: absolute; left: 54px; top: 720px; width: 280px;
    display: flex; align-items: center; justify-content: center; gap: 10px;
  }
  .brand-dot { width: 16px; height: 16px; border-radius: 50%; background: var(--leaf); flex: none; }
  .brand-name {
    font-family: "Poppins", sans-serif; font-weight: 700; font-size: 24px;
    color: var(--chalk); text-transform: uppercase; white-space: nowrap;
  }
</style>
</head>
<body>
  <main class="cover">
    <svg class="grunge" width="864" height="864" viewBox="0 0 864 864" aria-hidden="true">
      <filter id="rough-denim">
        <feTurbulence type="fractalNoise" baseFrequency="0.9" numOctaves="3" seed="7"/>
        <feColorMatrix type="saturate" values="0"/>
        <feComponentTransfer>
          <feFuncA type="table" tableValues="0 0.9"/>
        </feComponentTransfer>
      </filter>
      <filter id="scuffs">
        <feTurbulence type="turbulence" baseFrequency="0.012 0.05" numOctaves="2" seed="3"/>
        <feColorMatrix type="matrix" values="0 0 0 0 0  0 0 0 0 0  0 0 0 0 0  0 0 0 -2.2 1.1"/>
      </filter>
      <rect width="864" height="864" filter="url(#rough-denim)"/>
      <rect width="864" height="864" filter="url(#scuffs)" opacity=".5"/>
    </svg>

    <svg class="hosts-photo" width="864" height="864" viewBox="0 0 864 864" role="img" aria-label="Black and white photo of the two smiling podcast hosts in dark polo shirts">
      <defs>
        <linearGradient id="host-back" x1="0" y1="0" x2="0.3" y2="1">
          <stop offset="0" stop-color="var(--photo-light)"/>
          <stop offset="0.28" stop-color="var(--photo-mid)"/>
          <stop offset="1" stop-color="var(--photo-dark)"/>
        </linearGradient>
        <linearGradient id="host-front" x1="0.4" y1="0" x2="0.5" y2="1">
          <stop offset="0" stop-color="var(--photo-light)"/>
          <stop offset="0.3" stop-color="#6a6a6a"/>
          <stop offset="0.45" stop-color="#262626"/>
          <stop offset="1" stop-color="var(--photo-dark)"/>
        </linearGradient>
      </defs>
      <path fill="url(#host-back)" d="M744 12 C800 10 832 50 834 110 C836 160 826 200 812 228 C840 250 858 268 864 290 L864 864 L640 864 L660 420 C668 360 690 300 700 280 C690 240 680 200 680 140 C680 60 700 14 744 12 Z"/>
      <path fill="url(#host-front)" d="M612 216 C662 216 690 254 690 316 C690 370 676 400 662 440 C720 470 760 500 770 560 L800 864 L330 864 C336 800 344 720 360 620 C370 570 400 540 470 512 C510 494 540 480 560 460 C548 420 540 380 540 320 C540 256 566 216 612 216 Z"/>
    </svg>

    <svg class="frame-lines" width="864" height="864" viewBox="0 0 864 864" aria-hidden="true">
      <g fill="none" stroke="var(--leaf)" stroke-width="4">
        <polyline points="0,462 42,462 42,504 104,504"/>
        <polyline points="358,441 446,441 446,480 472,480"/>
      </g>
      <g fill="var(--leaf)">
        <circle cx="104" cy="504" r="7"/>
        <circle cx="358" cy="441" r="7"/>
      </g>
      <g fill="none" stroke="var(--chalk)" stroke-width="5">
        <polyline points="42,533 42,832 320,832"/>
        <polyline points="776,16 822,16 822,186"/>
      </g>
    </svg>

    <h1>
      <span class="title title-top">Coin</span>
      <span class="title title-bottom">Porchlight</span>
    </h1>

    <p class="tagline tagline-main">Money Tricks</p>
    <p class="tagline tagline-join">With a little</p>
    <p class="tagline tagline-end">Front-porch drawl</p>

    <div class="brand">
      <span class="brand-dot"></span>
      <span class="brand-name">Bright Harbor Plans</span>
    </div>
  </main>
</body>
</html>
```